Individual product brochures and one linecard

I am looking for 5 individual product brochures for our main product lines, and one full line card incorporating the 5. The products can be found at our website home page www.brightvalecnc.com (not including the parts and accessories). We cater to the CNC milling and machining industry, particularly in woods and plastics in industrial settings. We can provide many more additional images one placeholders are in place.

```html
<!DOCTYPE html>
<html lang="en">
<head>
<meta charset="utf-8">
<title>Brightvale CNC – Gasketing Brochures</title>
<link href="https://fonts.googleapis.com/css2?family=Poppins:wght@300;400;600;700&display=swap" rel="stylesheet">
<style>
  :root{
    --board:#e6e6e8;
    --paper:#ffffff;
    --teal:#208a7d;
    --teal-dark:#1b6a61;
    --ink:#2b2b2b;
    --on-teal:#e9f5f3;
  }
  *{box-sizing:border-box;margin:0;padding:0}
  html,body{width:932px;height:1200px;overflow:hidden;background:var(--board)}
  body{position:relative;font-family:'Poppins',sans-serif;color:var(--ink)}

  .page{position:absolute;width:361px;height:467px;background:var(--paper);overflow:hidden;box-shadow:0 2px 5px rgba(0,0,0,.18)}
  .page--grid{left:86px;top:141px}
  .page--inboard{left:485px;top:326px}
  .page--onboard{left:86px;top:637px}

  .hero{position:absolute;left:0;top:0;width:361px;height:141px;clip-path:polygon(0 0,100% 0,100% 89%,0 100%)}
  .hero--grid{background:linear-gradient(160deg,#6d5845 0%,#9a7e62 45%,#b99c7c 100%)}
  .hero--inboard{background:linear-gradient(170deg,#8c8a86 0%,#cfcbc4 50%,#55504a 100%)}
  .hero--onboard{background:linear-gradient(160deg,#8d7458 0%,#b09676 55%,#a08868 100%)}

  .title-box{position:absolute;left:17px;top:0;width:132px;height:78px;background:var(--teal);color:#fff;padding:14px 0 0 8px;font-size:14.5px;line-height:19px;letter-spacing:.2px}
  .title-box span{display:block;font-weight:300}
  .title-box strong{display:block;font-weight:700}

  .heading{position:absolute;left:26px;top:148px;font-size:11.5px;font-weight:700;color:var(--teal)}
  .heading-rule{position:absolute;left:26px;top:172px;width:48px;height:1px;background:var(--teal)}

  .intro{position:absolute;left:26px;top:182px;width:140px;font-size:4.6px;line-height:5.6px;font-weight:700;color:var(--teal)}
  .body{position:absolute;left:26px;width:140px;font-size:4.6px;line-height:5.6px;font-weight:400}

  .photo{position:absolute;left:193px;width:153px;height:75px}
  .photo--a{top:146px}
  .photo--b{top:229px}
  .photo--steel{background:linear-gradient(135deg,#c9ccce,#8f8e8a 60%,#6b5a4a)}
  .photo--table{background:linear-gradient(180deg,#e4e2de 0%,#9a9c9f 55%,#f2f2f2 100%)}
  .photo--fixture{background:linear-gradient(160deg,#e2d4bd,#cbb99c)}
  .photo--pine{background:linear-gradient(180deg,#ddc9a3,#c9ab78)}
  .photo--strip{background:linear-gradient(135deg,#c7b397,#3a3a3a 70%,#a89a88)}
  .photo--mdf{background:linear-gradient(160deg,#c8b79e,#b29f84)}

  .caption{position:absolute;left:193px;top:309px;width:150px;font-size:4.8px;line-height:5.8px;font-weight:700;color:var(--teal)}

  .diagram{position:absolute;background:linear-gradient(135deg,#f4f4f4,#d6d6d6);border:0.5px solid #c8c8c8}

  .panel{position:absolute;left:183px;top:325px;width:178px;height:142px;background:var(--teal);border-top-left-radius:9px;padding:6px 8px 0 11px}
  .checklist{list-style:none}
  .checklist li{position:relative;padding-left:11px;margin-bottom:4.4px;font-size:4.2px;line-height:5.2px;font-weight:300;color:var(--on-teal)}
  .checklist li::before{content:"";position:absolute;left:0;top:0;width:5px;height:5px;border-radius:50%;background:#fff}
  .checklist li::after{content:"";position:absolute;left:1.6px;top:1.1px;width:1.3px;height:2.3px;border-right:0.8px solid var(--teal);border-bottom:0.8px solid var(--teal);transform:rotate(40deg)}
  .checklist--dense li{margin-bottom:3.4px}

  .brand{position:absolute;left:26px;top:420px;display:flex;align-items:center;gap:4px;font-size:12px;font-weight:600;color:var(--teal-dark);line-height:1}
  .brand-mark{width:6px;height:6px;border-radius:50%;background:var(--teal-dark)}
  .site{position:absolute;left:26px;top:448px;font-size:5.2px;color:var(--teal);letter-spacing:.2px}

  .bullets{position:absolute;left:25px;top:307px;width:84px;list-style:none}
  .bullets li{position:relative;padding-left:6px;margin-bottom:4px;font-size:4.4px;line-height:5.4px}
  .bullets li::before{content:"";position:absolute;left:1px;top:2px;width:1.4px;height:1.4px;border-radius:50%;background:var(--teal)}
</style>
</head>
<body>

<!-- Grid Gasketing -->
<section class="page page--grid">
  <div class="hero hero--grid" role="img" aria-label="Close-up of a CNC router grid table with gasketed channels"></div>
  <div class="title-box"><span>THE ONLY</span><span>ANSWER FOR</span><strong>CNC GASKETS</strong></div>

  <h2 class="heading">Grid Gasketing</h2>
  <div class="heading-rule"></div>

  <p class="intro">Every CNC Router that is employing vacuum hold-down methods needs to incorporate some type of gasketing material. Most operators are familiar with the gasketing material that is placed in the outer most channel of their CNC router table. Many CNC Router training seminars will mention: "make sure to get some gasketing material to get good seal around your spoilboards". This gasketing material is essential to fill the void between the router table and the spoilboard, creating a quality vacuum clamp on the spoilboards. We call this material Grid Gasketing and getting the proper material for your machine is the first step. This is the "foundation of the house" so-to-speak.</p>

  <p class="body" style="top:261px">The ideal product will fill the channel width wise evenly and stick above the surface of the channel by roughly 1/16". We also feel as though a rounded channel should be fitted with a round gasket. Squared channels should be fitted with squared gasketing products. Brightvale CNC has a Grid Gasket product for each CNC Router Manufacturer. The proper Grid Gasketing product for a particular channel size is crucial to maximizing vacuum performance. Too narrow and it will slip in the channel. Too wide and it will pinch when trying to zero out on the z-depth.</p>

  <p class="body" style="top:324px">Different router manufacturers mill their channels at different dimensions. On top of that, we feel some router manufactures will either provide or recommend a particular size gasket for their own machine, but we find that these products may not be the ideal gasketing product to MAXIMIZE vacuum performance. First thing we always do when talking to a new customer is to ask them what type of router they have. This will help to get an idea of the best gasketing product to provide. But the list we have developed is only a guide. When looking for the best grid gasketing product for your machine, follow these guides:</p>

  <div class="photo photo--a photo--steel" role="img" aria-label="Router gantry above a gasketed grid table"></div>
  <div class="photo photo--b photo--table" role="img" aria-label="Full CNC router table fitted with grid gasketing"></div>

  <div class="panel">
    <ul class="checklist">
      <li>Square channels use square gasket products. Rounded channels and dove-tail channels use rounded gasket products.</li>
      <li>The gasketing should stick proud above the table by 1/16.</li>
      <li>Non-adhesive material is best. When it comes time to replace the gasketing there is not adhesive residue left behind in the channels.</li>
      <li>Replace the gasketing in your table like you would replace the oil in your car. For best results, this gasketing is creating a proper "base". If the gasketing wears and becomes flush with the table, it is time to replace it. A flush gasket is performing as well as no gasket.</li>
      <li>The GX 25 312 is the most commonly ordered product. It is ideal for the 1/4 x 1/4 channel that is so common in today's routers.</li>
    </ul>
  </div>

  <div class="brand"><span class="brand-mark"></span>Brightvale</div>
  <p class="site">WWW.BRIGHTVALECNC.COM/GRID-GASKETING/</p>
</section>

<!-- In Board Gasketing -->
<section class="page page--inboard">
  <div class="hero hero--inboard" role="img" aria-label="Dedicated vacuum fixture with rectangular gasket pockets"></div>
  <div class="title-box"><span>THE ONLY</span><span>ANSWER FOR</span><strong>CNC GASKETS</strong></div>

  <h2 class="heading">In Board Gasketing</h2>
  <div class="heading-rule"></div>

  <p class="intro">When routing repetitive parts, best solution may very well be to make a dedicated vacuum fixture. When using a non-porous fixture material, a vacuum source can be created for each piece, reducing vacuum loss. Using a non-porous fixture board also greatly reduces the vacuum loss that would occur through the sides and exposed tool paths of a porous board, like MDF. An adhesive backing keeps the gasketing material in the pre-routed channels.</p>

  <p class="body" style="top:238px">In-Board Gasketing is intended for long-term use applications. We call these dedicated fixtures as opposed to spoilboards. In-Board Gasketing is longer lasting than surface mounted gasketing because it is recessed into the fixture. When the vacuum is engaged, the gasketing can only compress down the the height of the fixture. We recommend a 3-to-1 ration in terms of how much sticking above the fixture surface.</p>

  <p class="body" style="top:289px">There are major benefits when it comes to In-Board Gasketing in a Dedicated Fixture:</p>

  <ul class="bullets">
    <li>Because the gasketing is recessed by roughly 75%, it can only compress by the remaing 25% that remains above the fixture. This gives the gaksketing (and dedicated fixture) extended lifetime.</li>
    <li>When the gasketing is pulled down into the channel, the part being routed is pulled flush against the fixture. This gives the part added rigidity when it is being route</li>
  </ul>

  <div class="diagram" style="left:119px;top:308px;width:52px;height:30px" role="img" aria-label="Diagram of in-board gasketing recessed in a fixture over a vacuum channel"></div>

  <div class="photo photo--a photo--fixture" role="img" aria-label="Fixture board with routed gasket channels"></div>
  <div class="photo photo--b photo--pine" role="img" aria-label="Wood fixture with gasket strips and vacuum holes"></div>
  <p class="caption">Some additional ideas to keep in mind when making a dedicated vacuum fixture:</p>

  <div class="panel">
    <ul class="checklist">
      <li>Make the fixture out of a non-porous material (Baltic Birch, HDPS, Melamine, etc.) so the fixture itself is not porous and leaking vacuum.</li>
      <li>Vacuum source holes are needed to port the vacuum from the grid table below to not only each part, but also the waste pieces.</li>
      <li>After the vacuum source is created, a slight recess into the fixture is needed to allow for the creating of a vacuum pocket area.</li>
      <li>Include a slight chamfer at the top of the gasketing channel so the gasketing does not pinch between the fixture and the part.</li>
      <li>SX 25 38 is the most common product ordered. Route this gasket channel 3/16 deep and 3/8 wide. It leaves 1/16 exposed above the channel.</li>
      <li>If your material has excess warp/variance, a thicker gasket like SX 38 38 or SX 50 50 would allow for more material sticking above the surface if we stick to that 3-to-1 ratio.</li>
    </ul>
  </div>

  <div class="brand"><span class="brand-mark"></span>Brightvale</div>
  <p class="site">WWW.BRIGHTVALECNC.COM/GRID-GASKETING/</p>
</section>

<!-- On-Board Gasketing -->
<section class="page page--onboard">
  <div class="hero hero--onboard" role="img" aria-label="MDF spoilboard with surface mounted gasket outlines being applied"></div>
  <div class="title-box"><span>THE ONLY</span><span>ANSWER FOR</span><strong>CNC GASKETS</strong></div>

  <h2 class="heading">On-Board Gasketing</h2>
  <div class="heading-rule"></div>

  <p class="intro">The quickest and easiest way to create a vacuum clamp is with On-Board Gasketing. It is an extremely quick and cost effective way to improve vacuum hold performance without having the spend the time or materials on making dedicated fixtures. create a vacuum clamp, the ideal solution is On-Board Gasketing. It is the easiest way to improve a vacuum hold down application on an MDF spoilboard vs downdraft hold only, and frankly it is not even a fair fight.</p>

  <p class="body" style="top:239px">When introducing gasketing, it changes the hold down environment from a simple downdraft system to a vacuum clamping, suction-cup style system. It is a different science. The vacuum clamp hold that is achieved with gasketing is 20X the vacuum pressure of a simple down-draft system. A simple flick of a finger can move a part on a MDF spoilboard, while a rubber mallet may not move a part out of place that is properly gasketed.</p>

  <div class="diagram" style="left:27px;top:300px;width:63px;height:33px" role="img" aria-label="Diagram of on-board gasketing with tool path, spoilboard and vacuum source"></div>

  <p class="body" style="top:352px;width:120px">A surface mounted gasket does not require any programming or channels. By utilizing a porous MDF spoilboard, vacuum source holes seen here would not be required either.</p>

  <div class="photo photo--a photo--strip" role="img" aria-label="Roll of thin gasket strip beside a coin on MDF"></div>
  <div class="photo photo--b photo--mdf" role="img" aria-label="Curved gasket line applied to an MDF spoilboard"></div>
  <p class="caption">A few things to consider when evaluating On-Board Gasketing Products:</p>

  <div class="panel">
    <ul class="checklist checklist--dense">
      <li>The thinner the better. Thinner surface mounted gasket creates less part vibration. But enough thickness is needed to counter-act the variances of the material looking to be held.</li>
      <li>It is why the 1/32 thick SX 03 material is the most common for plastics applications.</li>
      <li>The SX 06 material most common among woodworkers.</li>
      <li>The SX 12 material when working with materials that have a lot of variances.</li>
      <li>The SX 06 38 3/8 width is the most commonly ordered. Narrow widths (1/4 and 1/8) can help with tighter areas. Wider size like 1/2 and more are also available.</li>
      <li>Lower Density products (LD series) are typically ordered by customers with low-powered vacuum systems, such as home built machines and hobbyists.</li>
      <li>Firm Density Products (FD series) are for very heavy weight products that need a strong gasket to hold up under the weight of the material, not just vacuum pull.</li>
    </ul>
  </div>

  <div class="brand"><span class="brand-mark"></span>Brightvale</div>
  <p class="site">WWW.BRIGHTVALECNC.COM/GRID-GASKETING/</p>
</section>

</body>
</html>
```